Business Card Design Project - ol taviran group

dear Sirs

we need business card design for our group ( OL Taviran Group ) , i have got the Logo design of our group from pixel forum in previous , so all need details relating to our group i think available with you, as well as the the chosen logo design

we hope to provide us with business card logo that to be appropaite and satisfactory to us .

thanks

note : logo design of our group is attached .

Reason: please extend the deadline of my project for additional 15 days because i didn't received appropriate design for our gruop yet . kindly beaware that i have received 77 design till now , supossed to send me 200-250 design at least . thanks

contents

name : Selim OR Haddani

position : Operation Manager

• person name

group logo
• logo color matching with back background

```html
<!DOCTYPE html>
<html lang="en">
<head>
<meta charset="utf-8">
<title>OL Taviran Group – Business Cards</title>
<link rel="stylesheet" href="https://fonts.googleapis.com/css2?family=Montserrat:wght@400;500;600&display=swap">
<style>
  :root {
    --bg: #ece6d2;
    --card: #ffffff;
    --navy: #1f3f8f;
    --gold: #c9a24a;
    --gold-light: #e6cf8f;
    --ink: #333333;
    --muted: #555555;
  }
  * { margin: 0; padding: 0; box-sizing: border-box; }
  html, body { width: 1200px; height: 951px; overflow: hidden; }
  body {
    background: var(--bg);
    font-family: "Montserrat", sans-serif;
    position: relative;
  }
  .card {
    position: absolute;
    width: 600px;
    height: 345px;
    background: var(--card);
    border-radius: 22px;
    overflow: hidden;
    box-shadow: 0 6px 18px rgba(0,0,0,0.18);
  }
  .card-front { left: 90px; top: 90px; }
  .card-back { left: 510px; top: 520px; }
  .card svg.decor { position: absolute; inset: 0; }

  .brand {
    display: flex;
    align-items: center;
    gap: 14px;
    color: var(--navy);
    font-weight: 500;
    letter-spacing: 1px;
  }
  .brand-mark {
    width: 18px; height: 18px;
    background: var(--navy);
    flex: none;
  }
  .card-front .brand {
    position: absolute;
    left: 0; right: 0; top: 118px;
    justify-content: center;
    font-size: 46px;
  }
  .card-front .website {
    position: absolute;
    left: 0; right: 0; top: 232px;
    text-align: center;
    color: var(--navy);
    font-size: 17px;
    font-weight: 500;
    letter-spacing: 1.5px;
  }

  .card-back .brand {
    position: absolute;
    right: 50px; top: 52px;
    font-size: 32px;
  }
  .card-back .brand-mark { width: 14px; height: 14px; }
  .person { position: absolute; left: 46px; top: 120px; }
  .person-name { font-size: 21px; font-weight: 500; color: var(--ink); }
  .person-role { font-size: 14px; color: var(--gold); margin-top: 3px; }

  .address {
    position: absolute; left: 46px; top: 190px;
    display: flex; gap: 10px;
    font-size: 15px; line-height: 21px; color: var(--ink);
  }
  .contacts {
    position: absolute; left: 330px; top: 190px;
    list-style: none;
    font-size: 15px; line-height: 21px; color: var(--ink);
  }
  .contacts li { display: flex; align-items: center; gap: 10px; }
  .contacts .accent { color: var(--gold); }
  .icon { width: 14px; height: 14px; flex: none; fill: var(--gold); }
  .address .icon { margin-top: 3px; }
</style>
</head>
<body>

<section class="card card-front" aria-label="Business card front">
  <svg class="decor" width="600" height="345" viewBox="0 0 600 345" aria-hidden="true">
    <defs>
      <linearGradient id="goldBand" x1="0" x2="1">
        <stop offset="0" stop-color="#a98432"/>
        <stop offset="0.5" stop-color="#e6cf8f"/>
        <stop offset="1" stop-color="#b8913e"/>
      </linearGradient>
    </defs>
    <path d="M0 0 H26 Q58 172 26 345 H0 Z" fill="url(#goldBand)"/>
    <path d="M26 0 Q58 172 26 345" fill="none" stroke="#1f3f8f" stroke-width="4"/>
    <path d="M600 0 H574 Q542 172 574 345 H600 Z" fill="url(#goldBand)"/>
    <path d="M574 0 Q542 172 574 345" fill="none" stroke="#1f3f8f" stroke-width="4"/>
  </svg>
  <div class="brand"><span class="brand-mark"></span>OL Taviran Group</div>
  <p class="website">www.oltavirangroup.com</p>
</section>

<section class="card card-back" aria-label="Business card back">
  <svg class="decor" width="600" height="345" viewBox="0 0 600 345" aria-hidden="true">
    <path d="M0 0 H70 Q20 40 0 120 Z" fill="#1f3f8f"/>
    <path d="M0 130 Q30 40 105 0" fill="none" stroke="#c9a24a" stroke-width="6"/>
    <path d="M600 345 H520 Q575 300 600 215 Z" fill="#1f3f8f"/>
    <path d="M600 200 Q570 300 490 345" fill="none" stroke="#c9a24a" stroke-width="6"/>
  </svg>

  <div class="brand"><span class="brand-mark"></span>OL Taviran Group</div>

  <div class="person">
    <p class="person-name">Selim OR Haddani</p>
    <p class="person-role">Operation Manager</p>
  </div>

  <div class="address">
    <svg class="icon" viewBox="0 0 14 14" aria-hidden="true"><path d="M7 1 L13 6.5 H11 V13 H8.5 V9 H5.5 V13 H3 V6.5 H1 Z"/></svg>
    <p>1450 Orlen Park Rd.<br>Suite 204-118<br>Calden, TX 75910</p>
  </div>

  <ul class="contacts">
    <li><svg class="icon" viewBox="0 0 14 14" aria-hidden="true"><path d="M3 1 H6 L7 4 L5 5.5 Q6.5 8.5 8.5 9 L10 7 L13 8 V11 Q13 13 11 13 Q1 12 1 3 Q1 1 3 1 Z"/></svg>555-014-2290</li>
    <li><svg class="icon" viewBox="0 0 14 14" aria-hidden="true"><rect x="3" y="1" width="8" height="4"/><rect x="1" y="5" width="12" height="6" rx="1"/><rect x="3" y="10" width="8" height="3"/></svg>555-014-2291</li>
    <li><svg class="icon" viewBox="0 0 14 14" aria-hidden="true"><path d="M1 3 H13 V11 H1 Z M1 3 L7 8 L13 3" fill="none" stroke="#c9a24a" stroke-width="1.6"/></svg>info@<span class="accent">oltavirangroup</span>.com</li>
    <li><svg class="icon" viewBox="0 0 14 14" aria-hidden="true"><circle cx="7" cy="7" r="6"/></svg>www.<span class="accent">oltavirangroup</span>.com</li>
  </ul>
</section>

</body>
</html>
```